Flyer-Design für Bio Gemüsebau
Zielgruppe
Bio-Gemüseanbau: Bei uns gibt es über 45 Gemüsekulturen von Aubergine bis Zwiebeln.
Endverbraucher, Menschen, die sich gerne gesund ernähren und Wert auf Nachhaltigkeit und Regionalität legen.
Wir verkaufen am Straßenstand sowie an Abonnenten.
Wir heißen 'Gemüsehof Stiller Acker' und haben bereits ein Logo (siehe Anhang)
Aufgabenstellung
Es wäre prima, wenn der Flyer allgemeine Infos (siehe Worddatei) zu dem Gemüseangebot und der Gärtnerei enthält.
Wir werden zudem einige Fotos zur Auswahl beilegen.
Es wäre ganz toll, wenn an prominenter Stelle ein Foto Platz finden würde, an dessen Stelle man bei Bedarf z.B. auf eine Veranstaltung oder eine bestimmte Aktion hinweisen könnte. Also, dass wir bei Bedarf dieses Foto entfernen und diesen Platz für einen aktuellen Hinweis nutzen könnten.
Ansonsten sind wir offen, was das Format des Flyers angeht. Wenn das Design auf einem ökologischen Papier funktionieren könnte, wäre das super, da wir ja ein Biobetrieb sind.
Unser Logo muss auf jeden Fall mit drauf, das ist inzwischen schon etabliert.
Weitere Infos auf unserer Homepage www.gemuesehof-stilleracker-beispiel.de (unter Galerie sind auch weitere Fotos, die verwendet werden könnten)
Vielen Dank.

```html
<!DOCTYPE html>
<html lang="de">
<head>
<meta charset="utf-8">
<title>Gemüsehof Stiller Acker – Flyer</title>
<link rel="stylesheet" href="https://fonts.googleapis.com/css2?family=Amatic+SC:wght@700&family=Patrick+Hand&display=swap">
<style>
  :root{
    --backdrop:#d3d3d6;
    --paper:#ffffff;
    --brown:#6b3526;
    --brown-dark:#4e2518;
    --sky:#a9c6e2;
    --field:#6f7a52;
    --veg-green:#4f6b3a;
    --veg-red:#a8303e;
    --veg-orange:#e0782a;
  }
  *{margin:0;padding:0;box-sizing:border-box}
  html,body{width:841px;height:1200px;overflow:hidden;background:var(--backdrop)}
  body{position:relative;font-family:"Patrick Hand",cursive;color:var(--brown)}
  .page{position:absolute;left:10px;width:821px;background:var(--paper);overflow:hidden}
  .page--front{top:15px;height:584px}
  .page--back{top:609px;height:582px}
  .photo{position:absolute;inset:0}
  .photo--farmer{
    background:linear-gradient(180deg,var(--sky) 0%,#c7d9ea 38%,#8f9c6c 55%,var(--field) 75%,#5b4a3b 100%);
    clip-path:polygon(185px 0,821px 0,821px 584px,535px 584px,522px 560px,500px 530px,488px 500px,462px 468px,448px 430px,420px 398px,408px 360px,380px 325px,366px 290px,340px 255px,325px 215px,300px 182px,285px 145px,258px 110px,245px 70px,215px 40px);
  }
  .photo--harvest{
    background:linear-gradient(120deg,var(--veg-green) 0%,#5f7d45 30%,var(--veg-orange) 50%,var(--veg-red) 72%,#6b2a3a 100%);
    clip-path:polygon(0 0,575px 0,560px 40px,548px 80px,530px 118px,520px 160px,500px 200px,490px 245px,470px 285px,462px 330px,440px 372px,430px 415px,410px 455px,400px 500px,380px 540px,368px 582px,0 582px);
  }
  .heading{font-family:"Amatic SC",cursive;font-weight:700;color:var(--brown);letter-spacing:.5px}
  .brand{position:absolute;left:22px;top:150px;font-size:50px;line-height:52px;color:var(--brown-dark)}
  .intro-title{position:absolute;left:27px;top:290px;font-size:38px;line-height:40px}
  .intro-place{position:absolute;left:27px;top:331px;font-size:21px}
  .intro-text{position:absolute;left:27px;top:366px;font-size:15.5px;line-height:22px}
  .hours{position:absolute;left:27px;top:450px;font-size:17px;letter-spacing:.3px}
  .hours b{font-family:"Amatic SC",cursive;font-size:22px;margin-right:10px}
  .more{position:absolute;left:27px;top:484px;font-size:12.5px;line-height:17.5px}
  .url{position:absolute;left:27px;top:538px;font-size:18px}
  .basket{position:absolute;left:372px;top:443px;width:62px;height:68px;border-radius:8px;background:linear-gradient(180deg,#5c8a3c 0%,#e08a2e 45%,#8a5230 100%)}
  .cta{position:absolute;left:318px;top:500px;width:148px}
  .cta-jetzt{font-size:15px;display:block}
  .cta-main{font-size:34px;line-height:30px;display:block}
  .cta-sub{font-size:13px;display:block;text-align:right}
  .back-title{position:absolute;right:34px;top:16px;font-size:42px;line-height:42px;text-align:right}
  .back-text{position:absolute;right:34px;top:110px;width:320px;text-align:right;font-size:14.5px;line-height:19px}
  .back-text p{margin-bottom:18px}
  .facts{position:absolute;left:501px;top:320px;width:290px}
  .facts h3{font-size:24px;margin-bottom:4px;white-space:nowrap}
  .facts li{list-style:none;font-size:14.5px;line-height:20px;white-space:nowrap}
  .facts li::before{content:"· "}
  .contact{position:absolute;right:34px;top:468px;text-align:right;font-size:14.5px;line-height:19.5px;font-style:normal}
  .note{position:absolute;left:168px;top:294px;width:266px;height:254px;background:#fbfbfb;transform:rotate(-1.5deg);box-shadow:2px 3px 8px rgba(0,0,0,.35);padding:14px 18px}
  .note h4{font-size:21px;text-align:center;font-weight:400}
  .note .sub{font-size:11px;text-align:center;margin-top:-3px}
  .note .cols{display:flex;gap:20px;margin-top:14px;font-size:15.5px;line-height:22px}
  .note ul{list-style:none}
</style>
</head>
<body>
  <section class="page page--front">
    <div class="photo photo--farmer" role="img" aria-label="Foto: Gärtner mit Strohhut hält zwei Blumenkohlköpfe auf dem Gemüsefeld"></div>
    <h1 class="brand heading">Gemüsehof<br>Stiller Acker</h1>
    <h2 class="intro-title heading">Die Vielfaltsgärtnerei</h2>
    <p class="intro-place">in Nunkirchen</p>
    <p class="intro-text">Wir produzieren Gemüse im Einklang mit der Natur<br>für die Menschen vor Ort.<br>Unsere frischen Produkte gibt's am Straßenstand direkt am Feld.</p>
    <p class="hours"><b>ÖFFNUNGSZEITEN:</b>Sa 10-12, Fr 10-14</p>
    <p class="more">Wenn Du mehr wissen willst über unseren Anbau<br>(Market Gardening) und unser Gemüsesortiment<br>von A bis Z, besuche unsere Internetseite:</p>
    <p class="url">www.gemuesehof-stilleracker-beispiel.de</p>
    <div class="basket" role="img" aria-label="Symbol: Korb mit Gemüse"></div>
    <p class="cta"><span class="cta-jetzt">Jetzt</span><span class="cta-main heading">GEMÜSEKISTE</span><span class="cta-sub">abonnieren</span></p>
  </section>

  <section class="page page--back">
    <div class="photo photo--harvest" role="img" aria-label="Foto: frisch geerntetes Gemüse – Zucchini, Möhren, Rote und Gelbe Bete, Erbsen, Salat und Tomaten"></div>
    <div class="note">
      <h4>Inhalt der Abo-Kiste</h4>
      <p class="sub">(Beispiel aus Woche 33)</p>
      <div class="cols">
        <ul><li>1 Aubergine</li><li>500g Tomaten</li><li>1 Knollensellerie</li></ul>
        <ul><li>500g Möhren</li><li>1 Salatgurke</li><li>1 Salat</li><li>1 Spitzkohl</li><li>500g Zucchini</li><li>1 Bund Petersilie</li><li>300g Zwiebeln</li></ul>
      </div>
    </div>
    <h2 class="back-title heading">Gemüsekiste<br>abonnieren</h2>
    <div class="back-text">
      <p>Für eine ganze Saison kann man aber auch<br>eine Gemüsekiste bei uns abonnieren.</p>
      <p>Als Gemüsekisten-Abonnent leistest Du einen<br>wichtigen Beitrag für die regionale Landwirtschaft.</p>
      <p>Und Du bist sicher, jede Woche frisches Gemüse direkt<br>aus Nunkirchen zu erhalten und zahlst weniger als<br>beim Kauf am Stand.</p>
    </div>
    <div class="facts">
      <h3 class="heading">Abholkiste - kurz und knackig erklärt:</h3>
      <ul>
        <li>Jede Woche 8 bis 10 Gemüsesorten sowie Kräuter</li>
        <li>Abo von Mai bis Dezember</li>
        <li>20€ pro Woche</li>
        <li>Keine chemisch-synthetischen Dünger/Spritzmittel</li>
        <li>Abholung in Nunkirchen</li>
      </ul>
    </div>
    <address class="contact">Jonas Feldmann<br>Ackerweg 7<br>66000 Nunkirchen<br>(0151 2345 6789)<br>info@gemuesehof-stilleracker-beispiel.de</address>
  </section>
</body>
</html>
```